Bar and Grill looking or a Responsive Web design

New Bar and Grill in the Toronto area just opened up and is looking for a new wordpress website to start off his business.

Their business revolves around a homey family, upbeat atmosphere. His cuisine is gourmet pub style food. Speciality are home made burgers. 90 Seat restaurant in a very diverse and high density neighbourhood.

Looking for a responsive web design that will focus on a key feature pages.

Homepage
- Navigation is easy and simple, emphasize easy navigation in Mobile view.
- Contact information is a click or touch away

About Page

Menu Page
-Menu styling to be responsive. Very simple navigation through different menus and then menu would appear.

Gallery

Contact page
- Map (not trevlosk)
- Contact Details
- Contact/Feedback form

They do have a logo and will be uploaded.

We are open to any designs, as well as designs based off templates that have already been created.

Target Market(s)

Target audience is the varied. They are in an area that's densely populated and very diverse. Looking for a crowd that appreciates a setting for sports, good gourmet pub styled food and a home styled restaurant.

Industry/Entity Type

Restaurant

Colors

Designer to choose colors to be used in the design.

Requirements
Must have
• Menus have to have responsive design for both mobile and tablet/desktop.
Nice to have
• Easy access contact button on mobile view. That way it will act like a webapp so that mobile devices can take advantage of quick touches to get in contact.

```html
<!DOCTYPE html>
<html lang="en">
<head>
<meta charset="utf-8">
<title>Oakbarrow Bar &amp; Grill</title>
<link href="https://fonts.googleapis.com/css2?family=Ubuntu:ital,wght@0,400;0,500;0,700;1,500&family=Didact+Gothic&display=swap" rel="stylesheet">
<style>
:root{
  --green:#6f9422;
  --brown-dark:#3f1f0c;
  --brown:#4b250f;
  --brown-mid:#5a2c11;
  --brown-warm:#693514;
  --cream:#fdf7d3;
  --cream-deep:#f1e3a6;
  --orange:#e8a32a;
  --red-text:#e0542a;
  --price:#5d9621;
  --link-footer:#b2582a;
  --text-dark:#3b1c0a;
}
*{margin:0;padding:0;box-sizing:border-box}
html,body{width:1011px;height:1200px;overflow:hidden}
body{position:relative;font-family:'Ubuntu',sans-serif;background:var(--brown-dark);color:var(--text-dark)}
.abs{position:absolute}
a{color:inherit;text-decoration:none}

.topbar{left:0;top:0;width:1011px;height:21px;background:var(--green)}
.topbar .links{left:189px;top:6px;font-size:7px;color:#fff}
.topbar .links span{margin:0 3px}
.topbar .social{left:745px;top:5px;display:flex;gap:3px}
.topbar .social i{width:10px;height:10px;background:#fff;border-radius:1px;display:block}

.header{left:0;top:21px;width:1011px;height:64px;background:var(--brown)}
.brand{left:185px;top:16px;padding:6px 8px;font-size:22px;font-weight:500;color:var(--cream);letter-spacing:.5px;display:flex;align-items:center;gap:6px}
.brand b{width:8px;height:8px;border-radius:50%;background:var(--cream);display:block}
.contact{right:188px;top:11px;text-align:right;color:#fff;font-size:8px;line-height:10px}
.contact .phone{font-size:14px;line-height:20px}

.nav{left:0;top:85px;width:1011px;height:26px;background:var(--cream)}
.nav ul{left:189px;top:8px;display:flex;list-style:none;font-size:9.5px;color:#5b3015}
.nav li{margin-right:15.5px}
.nav li.active{font-weight:700;color:var(--text-dark)}
.search{left:728px;top:6px;width:94px;height:15px;background:var(--brown-dark);border-radius:3px;color:#cdb9a4;font-size:7.5px;font-style:italic;padding:3px 7px}
.search svg{position:absolute;right:5px;top:2px}

.hero{left:0;top:111px;width:1011px;height:304px;background:linear-gradient(90deg,#efe9dc 0%,#e3c8a8 25%,#d9b9ad 45%,#a7553f 70%,#5f3a25 90%,#c4a98a 100%)}
.hero-title{left:457px;top:193px;width:372px;height:46px;background:var(--brown);color:#fff;font-family:'Didact Gothic',sans-serif;font-size:34px;line-height:46px;text-align:center;border-radius:2px}
.hero-sub{left:512px;top:244px;width:317px;height:57px;background:var(--cream);color:var(--text-dark);font-family:'Didact Gothic',sans-serif;font-size:16px;line-height:20px;text-align:right;padding:9px 8px 0 0}
.arrow{top:239px;width:40px;height:40px;background:rgba(200,195,185,.85);display:flex;align-items:center;justify-content:center}

.features{left:0;top:415px;width:1011px;height:106px;background:var(--brown)}
.feature{top:17px;width:203px;height:77px;background:linear-gradient(var(--cream),#f8eebc);border:1px solid #d6c38a;border-radius:2px}
.feature svg{position:absolute;left:11px;top:17px}
.feature h3{position:absolute;left:54px;top:11px;font-weight:500;font-size:12px;color:var(--text-dark)}
.feature p{position:absolute;left:54px;top:29px;width:145px;font-size:7.5px;line-height:11px;color:var(--red-text)}
.feature .more{position:absolute;left:54px;top:57px;font-size:7.5px;color:#6b4a1a}

.thumbs{left:0;top:521px;width:1011px;height:107px;background:var(--cream)}
.thumb{top:9px;width:148px;height:88px;border:1px solid #e6dcc0;background:radial-gradient(ellipse at center,#e6a070 0%,#9cb25a 35%,#f5f4f0 60%,#fff 80%)}

.products{left:0;top:628px;width:1011px;height:240px;background:var(--brown-dark)}
.card{top:15px;width:147px;height:212px;background:var(--cream);border:1px solid #8a6a40;border-radius:2px;overflow:hidden}
.card .photo{height:100px}
.card h4{margin:8px 0 0 7px;font-size:9px;font-weight:700;color:var(--text-dark)}
.card p{margin:7px 6px 0 7px;font-size:7.5px;line-height:9.7px;color:#5a3a20}
.card .price{position:absolute;left:7px;top:169px;background:var(--price);color:#fff;font-size:8px;font-weight:700;padding:1px 7px}
.card .rating{position:absolute;right:9px;top:166px;text-align:right;font-size:6.5px;color:var(--text-dark);line-height:8px}
.card .rating em{font-style:normal;color:var(--price);letter-spacing:.5px}
.card .rating em b{color:var(--text-dark);font-weight:400}
.card .cta{position:absolute;left:0;bottom:0;width:100%;height:26px;background:var(--cream-deep);font-size:8px;font-weight:500;text-align:center;line-height:26px;color:#4a2a12}

.info{left:0;top:868px;width:1011px;height:139px;background:var(--brown-warm)}
.info h2{position:absolute;top:15px;font-size:12px;font-weight:700;color:var(--orange)}
.info .viewall{left:793px;top:17px;font-size:8px;color:#fff}
.info .txt{font-size:7.8px;line-height:9.7px;color:#fff}
.about-photo{left:188px;top:40px;width:94px;height:76px;border:1px solid #d8c7a8;background:linear-gradient(135deg,#2b1a12,#8a3a18 50%,#c47a30)}
.avatar{left:512px;width:39px;height:39px;border:1px solid #d8c7a8;background:linear-gradient(#d9b08c,#9a6b4a)}

.subscribe{left:0;top:1007px;width:1011px;height:42px;background:var(--brown)}
.subscribe .label{left:189px;top:16px;font-size:8px;color:#fff}
.subscribe .label b{color:var(--orange);font-weight:700;font-size:9px;margin-right:4px}
.email{left:566px;top:9px;width:148px;height:24px;background:var(--brown-dark);border-radius:2px;font-size:8px;font-style:italic;color:#8a5a3a;padding:7px 10px}
.sub-btn{left:727px;top:9px;width:95px;height:24px;background:var(--cream-deep);border-radius:2px;font-size:8px;font-weight:700;text-align:center;line-height:24px;color:var(--text-dark)}

.footer{left:0;top:1049px;width:1011px;height:128px;background:var(--brown-dark)}
.fcol{top:20px}
.fcol h5{font-size:8px;font-weight:700;color:#fff;margin-bottom:6px}
.fcol li{list-style:none;font-size:8px;line-height:16px;color:var(--link-footer)}
.fcol.nav-links li{line-height:20px}
.chef-box{left:621px;top:11px;width:201px;height:110px;background:var(--brown-warm);border-radius:2px}
.chef-box p{position:absolute;left:10px;top:18px;width:125px;font-size:8px;line-height:12px;color:#fff}
.chef-box .name{position:absolute;left:10px;top:81px;font-size:8px;line-height:12px;color:#fff}
.chef-box .name b{font-style:italic;font-weight:500}
.chef-figure{left:758px;top:2px;width:72px;height:110px;background:linear-gradient(#f4f1ea,#d7d2c8);border-radius:32px 32px 6px 6px}
.bottom{left:0;top:1177px;width:1011px;height:23px;background:#351a09;text-align:center;font-size:6.5px;line-height:23px;color:var(--link-footer)}
</style>
</head>
<body>

<div class="abs topbar">
  <div class="abs links">Our Dishes<span>|</span>Recipes<span>|</span>Our Menu<span>|</span>Sitemap</div>
  <div class="abs social" aria-label="Social links"><i></i><i></i><i></i><i></i><i></i><i></i></div>
</div>

<header class="abs header">
  <div class="abs brand"><b></b>OAKBARROW</div>
  <div class="abs contact">This is Pixelcraft's<br>version of Lorem Ipsum.<div class="phone">0000 000 000</div></div>
</header>

<nav class="abs nav">
  <ul class="abs">
    <li class="active">Home</li><li>Our Services</li><li>Recipes</li><li>Photo Gallery</li><li>Map Guide</li><li>About us</li><li>Contact us</li>
  </ul>
  <div class="abs search">Search here...
    <svg width="11" height="11" viewBox="0 0 11 11"><circle cx="4.5" cy="4.5" r="3.5" fill="none" stroke="#fff" stroke-width="1.4"/><line x1="7" y1="7" x2="10" y2="10" stroke="#fff" stroke-width="1.6"/></svg>
  </div>
</nav>

<section class="abs hero" role="img" aria-label="Home made burger with grilled steak and greens on a plate"></section>
<div class="abs hero-title">HOME MADE BURGERS</div>
<div class="abs hero-sub">PROIN GRAVIDA NIBH VEL VELIT<br>AUCTOR ALIQUET AENEAN SOLIDIN.</div>
<div class="abs arrow" style="left:51px"><svg width="12" height="16"><polyline points="9,2 3,8 9,14" fill="none" stroke="#fff" stroke-width="2.5"/></svg></div>
<div class="abs arrow" style="left:905px"><svg width="12" height="16"><polyline points="3,2 9,8 3,14" fill="none" stroke="#fff" stroke-width="2.5"/></svg></div>

<section class="abs features">
  <div class="abs feature" style="left:189px">
    <svg width="32" height="42" viewBox="0 0 32 42"><path d="M2 4 H30 L16 20 Z" fill="none" stroke="#3b1c0a" stroke-width="2"/><line x1="16" y1="20" x2="16" y2="38" stroke="#3b1c0a" stroke-width="2"/><line x1="8" y1="39" x2="24" y2="39" stroke="#3b1c0a" stroke-width="2.5"/><circle cx="21" cy="8" r="2" fill="#3b1c0a"/></svg>
    <h3>ENJOY HERE</h3>
    <p>This is Pixelcraft's version of Lorem Ipsum. Proin gravida nibh vel velit.</p>
    <span class="more">Learn more »</span>
  </div>
  <div class="abs feature" style="left:403px">
    <svg width="32" height="54" viewBox="0 0 32 54" style="top:13px"><path d="M4 2 V14 Q4 20 8 20 Q12 20 12 14 V2 M8 2 V14" fill="none" stroke="#3b1c0a" stroke-width="2"/><rect x="6.5" y="19" width="3" height="32" rx="1.5" fill="#3b1c0a"/><path d="M22 2 Q28 8 27 26 H24 V51 H21 Z" fill="#3b1c0a"/></svg>
    <h3>HUGE DINING SPACE</h3>
    <p>This is Pixelcraft's version of Lorem Ipsum. Proin gravida nibh vel velit.</p>
    <span class="more">Learn more »</span>
  </div>
  <div class="abs feature" style="left:619px">
    <svg width="32" height="50" viewBox="0 0 32 50" style="top:14px"><rect x="11" y="2" width="10" height="6" rx="3" fill="#3b1c0a"/><line x1="4" y1="11" x2="28" y2="11" stroke="#3b1c0a" stroke-width="2"/><circle cx="16" cy="16" r="4" fill="none" stroke="#3b1c0a" stroke-width="2"/><rect x="9" y="22" width="14" height="20" rx="6" fill="#3b1c0a"/><rect x="13" y="40" width="6" height="9" rx="3" fill="#3b1c0a"/></svg>
    <h3>HOME DELIVERY</h3>
    <p>This is Pixelcraft's version of Lorem Ipsum. Proin gravida nibh vel velit.</p>
    <span class="more">Learn more »</span>
  </div>
</section>

<section class="abs thumbs">
  <div class="abs thumb" style="left:188px" role="img" aria-label="Plated seafood salad"></div>
  <div class="abs thumb" style="left:350px" role="img" aria-label="Plated salmon with lemon and olives"></div>
  <div class="abs thumb" style="left:512px" role="img" aria-label="Grilled salmon with vegetables"></div>
  <div class="abs thumb" style="left:674px" role="img" aria-label="Grilled fish on greens"></div>
</section>

<section class="abs products">
  <article class="abs card" style="left:189px">
    <div class="photo" role="img" aria-label="Sliced roast beef with vegetables" style="background:linear-gradient(135deg,#6a2a1a,#a84a3a 50%,#3e6a1e)"></div>
    <h4>PROIN GRAVIDA</h4>
    <p>Nibh vel velit auctor aliquet. Aenean sollicitudin, lorem quis bibendum uctor, nisi elit consequat ipsum, nec sagittis sem nibh id elit.</p>
    <span class="price">$ 56</span>
    <div class="rating">34 Ratings<br><em>★★★★<b>★</b></em></div>
    <div class="cta">LEARN MORE</div>
  </article>
  <article class="abs card" style="left:351px">
    <div class="photo" role="img" aria-label="Grilled patties with corn and dip" style="background:linear-gradient(135deg,#ddd8cc,#6a3a20 45%,#8a5a2a 70%,#c8a030)"></div>
    <h4>GRAVIDA IPSUM</h4>
    <p>Nibh vel velit auctor aliquet. Aenean sollicitudin, lorem quis bibendum uctor, nisi elit consequat ipsum.</p>
    <span class="price">$ 64</span>
    <div class="rating">45 Ratings<br><em>★★★★<b>★</b></em></div>
    <div class="cta">LEARN MORE</div>
  </article>
  <article class="abs card" style="left:512px">
    <div class="photo" role="img" aria-label="Burger with potato wedges" style="background:linear-gradient(180deg,#5a4a3a,#c88a40 40%,#5a2a18 70%,#e0d8c8)"></div>
    <h4>PROIN LOREM</h4>
    <p>Nibh vel velit auctor aliquet. Aenean sollicitudin, lorem quis bibendum uctor, nisi elit consequat ipsum, nec sagittis.</p>
    <span class="price">$ 48</span>
    <div class="rating">30 Ratings<br><em>★★★★<b>★</b></em></div>
    <div class="cta">LEARN MORE</div>
  </article>
  <article class="abs card" style="left:674px">
    <div class="photo" role="img" aria-label="Burger with fries and corn" style="background:linear-gradient(135deg,#3a2a1a,#c89040 40%,#e8c030 75%,#f0e0a0)"></div>
    <h4>PROIN GRAVIDA</h4>
    <p>Nibh vel velit auctor aliquet. Aenean sollicitudin, lorem quis bibendum uctor, nisi elit consequat ipsum, nec sagittis sem nibh id elit.</p>
    <span class="price">$ 34</span>
    <div class="rating">24 Ratings<br><em>★★★★<b>★</b></em></div>
    <div class="cta">LEARN MORE</div>
  </article>
</section>

<section class="abs info">
  <h2 style="left:189px">ABOUT US</h2>
  <div class="abs about-photo" role="img" aria-label="Restaurant dining room interior"></div>
  <div class="abs txt" style="left:296px;top:40px;width:200px">This is Pixelcraft's version of Lorem Ipsum. Proin gravida nibh vel velit auctor aliquet. Aenean sollicitudin, lorem quis bibendum auctor, nisi elit consequat ipsum, nec sagittis sem nibh id elit.</div>
  <div class="abs txt" style="left:296px;top:89px;width:205px">Duis sed odio sit amet nibh vulputate cursus a sit amet mauris. Morbi accumsan ipsum velit.<br>Nam nec tellus a odio tincidunt auctor a ornare odio.</div>

  <h2 style="left:512px">TESTIMONIALS</h2>
  <span class="abs viewall">View all</span>
  <div class="abs avatar" style="top:40px" role="img" aria-label="Customer portrait"></div>
  <div class="abs txt" style="left:566px;top:40px;width:256px">“This is Pixelcraft's version of Lorem Ipsum. Proin gravida nibh vel velit auctor aliquet. Aenean sollicitudin, lorem quis bibendum auctor, nisi elit consequat ipsum, nec sagittis sem nibh id elit.”</div>
  <div class="abs avatar" style="top:86px" role="img" aria-label="Customer portrait"></div>
  <div class="abs txt" style="left:566px;top:89px;width:256px">“Duis sed odio sit amet nibh vulputate cursus a sit amet mauris. Morbi accumsan ipsum velit.Nam nec tellus a odio tincidunt auctor a ornare odio. Sed non mauris vitae.”</div>
</section>

<section class="abs subscribe">
  <div class="abs label"><b>SUBSCRIBE US</b>Proin gravida nibh vel velit auctor aliquet Proin gravida nibh vel velit.</div>
  <div class="abs email">Email Address</div>
  <div class="abs sub-btn">SUBSCRIBE</div>
</section>

<footer class="abs footer">
  <div class="abs fcol nav-links" style="left:189px"><h5>NAVIGATION</h5><ul><li>Home</li><li>Servises</li><li>Recipes</li><li>Contact us</li></ul></div>
  <div class="abs fcol" style="left:296px"><h5>GRILLS</h5><ul><li>Pixelcraft's</li><li>version</li><li>Lorem Ipsum</li><li>Proin gravida</li><li>Nibh vel velit</li></ul></div>
  <div class="abs fcol" style="left:404px"><h5>OUR BAR SPECIAL</h5><ul><li>Pixelcraft's version</li><li>Lorem Ipsum</li><li>Proin gravida</li></ul></div>
  <div class="abs fcol" style="left:512px"><h5>OUR BAR SPECIAL</h5><ul><li>Pixelcraft's version</li><li>Lorem Ipsum</li><li>Proin gravida</li><li>Nibh vel velit auctor</li><li>Aaliquet Aenean</li></ul></div>
  <div class="abs chef-box">
    <p>This is Pixelcraft's version of Lorem Ipsum. Proin gravida nibh vel velit auctor aliquet. Aenean sollicitudin.</p>
    <div class="name"><b>Martin Hale</b><br>Chief Shef</div>
  </div>
  <div class="abs chef-figure" role="img" aria-label="Head chef in white uniform"></div>
</footer>
<div class="abs bottom">Copyright 2013 &nbsp;|&nbsp; Bar &amp; Grill &nbsp;|&nbsp; All right reserved &nbsp;|&nbsp; Privacy Policy</div>

</body>
</html>
```